Pelton|Marsh & Quillan business card contest

We need a logo for an upscale boutique diversified company involved in real estate, investments, cattle, and more. Our businesses DO NOT need to be reflected in the business card nor do we want them noted. This is our logo and colors and we love our logo and colors. Our logo looks best against a black background and we like to include the firm name in our logo usage. importantly, the names Pelton and Marsh are separated by | not / and we use an ampersand not the word and.
On the front of the card, we want to include:
company logo and name (Pelton|Marsh & Quillan)
on the back, we would definitely include:
address, email, cell #
logo and name (smaller size than front)

The variable will be location of individual name and title (mine for example is ) - whether on the front OR on the back. interested in variations from which to choose
Dr. Neil R. Whitcombe, CFA
Scientifique des Fusées Financières

we would like to use contemporary symbols for address, email address, cell # with an option for web site that we do not intend to use initially. we like two sided cards and believe this design should use four rounded corners with the standard size. we prefer thicker card stock and may look at metal.

```html
<!DOCTYPE html>
<html lang="en">
<head>
<meta charset="utf-8">
<title>Pelton|Marsh &amp; Quillan – Business Card</title>
<link rel="stylesheet" href="https://fonts.googleapis.com/css2?family=Saira+Semi+Condensed:wght@500;700&display=swap">
<style>
  :root {
    --canvas: #2b2d30;
    --card: #141414;
    --card-edge: #1d1d1d;
    --orange: #f0891c;
    --grey: #8c8c8c;
    --white: #f2f2f2;
    --contact: #9a9a9a;
  }
  * { box-sizing: border-box; margin: 0; padding: 0; }
  html, body {
    width: 1200px; height: 1000px; overflow: hidden;
    background: var(--canvas);
    font-family: "Saira Semi Condensed", "Arial Narrow", sans-serif;
  }
  .canvas { position: relative; width: 1200px; height: 1000px; }
  .card {
    position: absolute; left: 250px; width: 700px; height: 400px;
    border-radius: 26px;
    background: linear-gradient(160deg, var(--card-edge), var(--card) 60%);
    box-shadow: 0 12px 30px rgba(0,0,0,.45);
    overflow: hidden;
  }
  .card--front { top: 50px; }
  .card--back { top: 540px; }

  /* Firm signature: invented name with one plain square */
  .firm { display: flex; align-items: center; color: var(--grey); font-weight: 500; white-space: nowrap; }
  .firm__square { background: var(--orange); flex: none; }

  .card--front .firm {
    position: absolute; left: 0; right: 0; top: 0; bottom: 0;
    justify-content: center; gap: 18px; font-size: 42px;
  }
  .card--front .firm__square { width: 46px; height: 46px; }

  .card--back .firm {
    position: absolute; left: 34px; top: 178px; gap: 10px; font-size: 21px;
  }
  .card--back .firm__square { width: 24px; height: 24px; }

  .divider {
    position: absolute; left: 336px; top: 52px; width: 3px; height: 296px;
    background: var(--white);
    transform: skewX(-8deg);
  }
  .person { position: absolute; left: 370px; top: 64px; }
  .person__name { color: var(--orange); font-weight: 700; font-size: 26px; line-height: 1.1; }
  .person__title { color: var(--white); font-weight: 700; font-size: 17px; margin-top: 2px; }

  .contacts { position: absolute; left: 370px; top: 160px; list-style: none; }
  .contacts li {
    display: flex; align-items: flex-start; gap: 14px;
    color: var(--contact); font-weight: 500; font-size: 17px; line-height: 1.25;
    margin-bottom: 9px;
  }
  .contacts svg { width: 18px; height: 18px; flex: none; margin-top: 2px; }
  .icon { fill: none; stroke: var(--orange); stroke-width: 1.8; stroke-linecap: round; stroke-linejoin: round; }
</style>
</head>
<body>
<main class="canvas">

  <section class="card card--front" aria-label="Card front">
    <div class="firm">
      <span class="firm__square"></span>
      <span class="firm__name">Pelton|Marsh &amp; Quillan</span>
    </div>
  </section>

  <section class="card card--back" aria-label="Card back">
    <div class="firm">
      <span class="firm__square"></span>
      <span class="firm__name">Pelton|Marsh &amp; Quillan</span>
    </div>

    <div class="divider"></div>

    <div class="person">
      <p class="person__name">Dr. Neil R. Whitcombe, CFA</p>
      <p class="person__title">Scientifique des Fusées Financières</p>
    </div>

    <ul class="contacts">
      <li>
        <svg viewBox="0 0 24 24"><path class="icon" d="M5 3h4l2 5-2.5 1.5a11 11 0 0 0 6 6L16 13l5 2v4a2 2 0 0 1-2 2A16 16 0 0 1 3 5a2 2 0 0 1 2-2z"/></svg>
        <span>1234567890</span>
      </li>
      <li>
        <svg viewBox="0 0 24 24"><rect class="icon" x="2.5" y="5" width="19" height="14" rx="1.5"/><path class="icon" d="M3 6l9 7 9-7"/></svg>
        <span>email@.com</span>
      </li>
      <li>
        <svg viewBox="0 0 24 24"><circle class="icon" cx="12" cy="12" r="9.5"/><ellipse class="icon" cx="12" cy="12" rx="4" ry="9.5"/><path class="icon" d="M2.5 12h19M4 7h16M4 17h16"/></svg>
        <span>www.website.com</span>
      </li>
      <li>
        <svg viewBox="0 0 24 24"><path class="icon" d="M12 22s7-7 7-12a7 7 0 0 0-14 0c0 5 7 12 7 12z"/><circle class="icon" cx="12" cy="10" r="2.5"/></svg>
        <span>Abc 234, Any street 345,<br>Any town</span>
      </li>
    </ul>
  </section>

</main>
</body>
</html>
```